Permanent Makeup (cosmetics salon) Brochure

We need a 2-4 sites brochure for our Permanent Makeup (cosmetics salon). Our company is based in Austria / Vienna. -> Our homepage is www.mk-lorenzhuber.at
This brochure should show which treatments we provide ot our customers.

I've uploaded our old brochure, the content (text) would be nearly the same (look form "Must Haves", pics have to be new (look uploaded pics)
The old brochure is to dark. -> look for our homepage maybe you can make it like this

Target Market(s)

woman, age 25-70 years who wants to have permanent makeup on eyebrows, lips or eyeliner

Industry/Entity Type

Beauty Salon

Requirements
Must have
• pics which are uploaded.

*This text (somithing about our business)
"Für Frau Lorenzhuber ist Permanent Makeup ein Kunsthandwerk. Das Team von MK-Lorenzhuber ist spezialisiert auf natürliches Permanent Makeup damit der individuelle Typ jeder Kundin am schönsten zum Ausdruck kommt."

*We do this treatments: (english)
+ Augenbrauen Microblading (eyebrows)
+ Augenbrauen Permanent Makeup (eyebrows2)
+ Lidstrich Permanent Makeup (eyeliner)
+ Lip Blushing (lips)
+ Lippen Permanent Makeup (lips2)

* Our addresses (2 locations)
Wien
Kerngasse 7b/12, 1010 Wien
Tel: 01/5827316

Villach
Birkenhofweg 24, 9524 St. Ulrich
Tel: 0676/3158940

Mail: info@mk-lorenzhuber.at
www.mk-lorenzhuber.at

```html
<!DOCTYPE html>
<html lang="de">
<head>
<meta charset="utf-8">
<title>Marika Lorenzhuber – Permanent Makeup Flyer</title>
<link href="https://fonts.googleapis.com/css2?family=Figtree:wght@400;500;700&family=Barlow+Condensed:wght@600&display=swap" rel="stylesheet">
<style>
  :root{
    --page:#ececec;
    --paper:#ffffff;
    --ink:#2a2522;
    --gold:#e9c85f;
    --gold-light:#f6dc7a;
    --gold-deep:#cfa946;
    --skin-1:#c7b0a2;
    --skin-2:#e4d3c7;
    --white:#ffffff;
  }
  *{margin:0;padding:0;box-sizing:border-box}
  html,body{width:1200px;height:764px;overflow:hidden;background:var(--page)}
  body{font-family:"Figtree",Arial,sans-serif;color:var(--ink)}
  .flyer-frame{position:absolute;left:352px;top:32px;width:495px;height:700px;box-shadow:0 6px 22px rgba(0,0,0,.12)}
  .flyer{position:absolute;left:0;top:0;width:920px;height:1300px;transform:scale(.538);transform-origin:0 0;background:var(--paper);overflow:hidden}
  .flyer-bg{position:absolute;inset:0}
  .brand{position:absolute;left:50px;top:30px;width:400px;display:flex;align-items:center;justify-content:center;gap:16px}
  .brand-name{font-size:34px;font-weight:500;color:var(--ink);letter-spacing:.5px}
  .brand-dot{width:62px;height:62px;border-radius:50%;background:var(--gold);flex:none}
  .tagline{position:absolute;left:0;width:490px;top:108px;text-align:center;font-family:"Barlow Condensed",Arial,sans-serif;font-weight:600;font-size:15px;letter-spacing:1.2px;color:var(--ink)}
  .intro{position:absolute;left:42px;top:147px;width:421px;font-size:17.4px;line-height:22.5px;text-align:justify}
  .contact{position:absolute;left:585px;top:458px;width:290px;height:290px;border-radius:50%;background:radial-gradient(circle at 40% 35%,var(--gold-light),var(--gold) 70%,var(--gold-deep));box-shadow:0 0 0 16px var(--white);display:flex;flex-direction:column;align-items:center;justify-content:center;text-align:center}
  .contact-icons{display:flex;gap:8px;margin-bottom:10px}
  .contact-line{font-size:21.5px;line-height:27px;font-weight:500}
  .service{position:absolute;width:250px;text-align:center}
  .service-photo{display:block;width:224px;height:224px;margin:0 auto;border-radius:50%;border:8px solid var(--gold);background:radial-gradient(circle at 45% 40%,var(--skin-2),var(--skin-1))}
  .service-photo.lips{background:radial-gradient(ellipse at 50% 55%,#e7978f,#efc2b2 60%,#f3d8cb)}
  .service-name{margin-top:8px;font-size:24px;line-height:30px}
  .addresses-title{position:absolute;left:65px;top:1195px;font-size:24px;font-weight:700;letter-spacing:-.3px}
  .addresses-line{position:absolute;left:55px;top:1259px;font-size:20.5px;white-space:nowrap}
  .addresses-line .sep{margin:0 18px}
</style>
</head>
<body>
<div class="flyer-frame">
  <div class="flyer">
    <svg class="flyer-bg" viewBox="0 0 920 1300" width="920" height="1300" aria-hidden="false">
      <defs>
        <linearGradient id="skin" x1="0" y1="0" x2="1" y2="0">
          <stop offset="0" stop-color="#c9b3a5"/>
          <stop offset=".55" stop-color="#dccabd"/>
          <stop offset="1" stop-color="#cdb5a6"/>
        </linearGradient>
        <linearGradient id="gold" x1="0" y1="0" x2="1" y2="0">
          <stop offset="0" stop-color="#f6dc7a"/>
          <stop offset="1" stop-color="#e2be55"/>
        </linearGradient>
      </defs>
      <rect role="img" aria-label="Photo: woman with closed eyes having pink eyeshadow applied with a brush" x="0" y="0" width="920" height="640" fill="url(#skin)"/>
      <path d="M0 272 C260 240 480 330 640 470 L780 600 L920 640 L920 1300 L0 1300 Z" fill="#cfa946"/>
      <path d="M0 305 C270 280 490 380 650 510 L770 600 L920 650 L920 1300 L0 1300 Z" fill="url(#gold)"/>
      <path d="M0 430 C260 380 460 450 600 540 L700 600 L920 650 L920 1300 L0 1300 Z" fill="#ffffff"/>
      <path d="M0 1230 C250 1180 500 1170 920 1230 L920 1300 L0 1300 Z" fill="url(#gold)"/>
    </svg>

    <div class="brand">
      <span class="brand-name">Marika</span>
      <span class="brand-dot"></span>
      <span class="brand-name">Lorenzhuber</span>
    </div>
    <div class="tagline">WAS IHNEN WERTVOLL IST, GEHÖRT IN GUTE HÄNDE</div>
    <p class="intro">Für Frau Lorenzhuber ist Permanent Makeup ein Kunsthandwerk. Das Team von MK-Lorenzhuber ist spezialisiert auf natürliches Permanent Makeup damit der individuelle Typ jeder Kundin am schönsten zum Ausdruck kommt</p>

    <div class="contact">
      <div class="contact-icons">
        <svg width="34" height="34" viewBox="0 0 34 34" aria-label="Telefon" role="img"><circle cx="17" cy="17" r="15" fill="none" stroke="#2a2522" stroke-width="2"/><path d="M12 9 l4 4 -2 2 c1 2 3 4 5 5 l2 -2 4 4 -2 3 c-7 -1 -13 -7 -14 -14 z" fill="#2a2522"/></svg>
        <svg width="34" height="34" viewBox="0 0 34 34" aria-label="E-Mail" role="img"><circle cx="17" cy="17" r="15" fill="none" stroke="#2a2522" stroke-width="2"/><rect x="9" y="11.5" width="16" height="11" fill="#2a2522"/><path d="M9 12 L17 18 L25 12" fill="none" stroke="#e9c85f" stroke-width="1.5"/></svg>
        <svg width="34" height="34" viewBox="0 0 34 34" aria-label="Web" role="img"><circle cx="17" cy="17" r="15" fill="none" stroke="#2a2522" stroke-width="2"/><circle cx="17" cy="17" r="9" fill="none" stroke="#2a2522" stroke-width="1.6"/><ellipse cx="17" cy="17" rx="4" ry="9" fill="none" stroke="#2a2522" stroke-width="1.6"/><path d="M8 17 H26 M10 12 H24 M10 22 H24" stroke="#2a2522" stroke-width="1.4"/></svg>
      </div>
      <div class="contact-line">0676/3158940</div>
      <div class="contact-line">info@mk-lorenzhuber.at</div>
      <div class="contact-line">www.mk-lorenzhuber.at</div>
    </div>

    <div class="service" style="left:38px;top:570px">
      <span class="service-photo" role="img" aria-label="Photo: close-up of a natural eyebrow"></span>
      <div class="service-name">Augenbrauen<br>Microblading</div>
    </div>
    <div class="service" style="left:302px;top:570px">
      <span class="service-photo" role="img" aria-label="Photo: young woman with defined eyebrows"></span>
      <div class="service-name">Augenbrauen<br>Permanent Makeup</div>
    </div>
    <div class="service" style="left:38px;top:876px">
      <span class="service-photo" role="img" aria-label="Photo: close-up of an eye with eyeliner"></span>
      <div class="service-name">Lidstrich<br>Permanent Makeup</div>
    </div>
    <div class="service" style="left:302px;top:876px">
      <span class="service-photo lips" role="img" aria-label="Photo: close-up of soft pink lips"></span>
      <div class="service-name">Lip<br>Blushing</div>
    </div>
    <div class="service" style="left:565px;top:876px">
      <span class="service-photo lips" role="img" aria-label="Photo: close-up of coral lips"></span>
      <div class="service-name">Lippen<br>Permanent Makeup</div>
    </div>

    <div class="addresses-title">OUR ADDRESSES</div>
    <div class="addresses-line">Wien, Kerngasse 7b/12, 1010 Wien<span class="sep">|</span>Villach, Birkenhofweg 24, 9524 St. Ulrich</div>
  </div>
</div>
</body>
</html>
```